Calvorn - Business Card Design

Design a modern masculine business card for our business

Target Market(s)

Private Market

Industry/Entity Type

Construction

Contact Information for Business Card

Company Name - Name of Person - Address - email address - contact number

Font styles to use
Serif
Sans Serif

Colors
0094D4
00A9DD
6FCCEA
C7EBF8
E9F6FB
00AB8E
00BBA5
67D7C9
C6EFE9
E9F9F6
F0912C
F2A743
F7CA91
FBE8D2
FDF5EE

Requirements
Must have
• Use company logo provided
Nice to have
• Company Logo

```html
<!DOCTYPE html>
<html lang="en">
<head>
<meta charset="utf-8">
<title>Calvorn Construction – Business Card</title>
<link rel="stylesheet" href="https://fonts.googleapis.com/css2?family=Montserrat:wght@300;400;700&display=swap">
<style>
  :root {
    --backdrop: #161616;
    --card: #262626;
    --accent: #f07a2e;
    --ink: #ffffff;
  }
  * { margin: 0; padding: 0; box-sizing: border-box; }
  html, body {
    width: 1200px; height: 900px; overflow: hidden;
    background: var(--backdrop);
    font-family: "Montserrat", Arial, sans-serif;
    color: var(--ink);
  }
  .canvas { position: relative; width: 1200px; height: 900px; }
  .card {
    position: absolute; left: 100px; top: 165px;
    width: 1000px; height: 570px;
    background: var(--card);
    box-shadow: 0 20px 50px rgba(0,0,0,.6);
    overflow: hidden;
  }
  .brand {
    position: absolute; left: 200px; top: 70px;
    display: flex; align-items: center; gap: 16px;
  }
  .brand-mark { width: 22px; height: 22px; background: var(--accent); }
  .brand-name {
    font-weight: 700; font-size: 64px; letter-spacing: 4px;
    text-transform: uppercase; line-height: 1; color: var(--ink);
  }
  .brand-sub {
    position: absolute; left: 238px; top: 148px;
    font-weight: 700; font-size: 17px; letter-spacing: 3px;
    text-transform: uppercase; color: var(--ink);
  }
  .contact {
    position: absolute; left: 110px; top: 240px;
    font-weight: 400; font-size: 22px; line-height: 1.5;
  }
  .address { margin-bottom: 12px; padding-left: 32px; }
  .contact-line { display: flex; align-items: center; gap: 12px; }
  .contact-line svg { width: 20px; height: 20px; flex: none; }
  .person {
    position: absolute; right: 130px; top: 395px; text-align: right;
  }
  .person-name {
    font-weight: 700; font-size: 30px; letter-spacing: 1px; line-height: 1.2;
    text-transform: uppercase; color: var(--accent);
  }
  .person-title { font-weight: 300; font-size: 24px; line-height: 1.3; }
  .person-bar {
    position: absolute; right: 92px; top: 400px;
    width: 14px; height: 66px; background: var(--accent);
  }
  .hazard-strip { position: absolute; left: 340px; bottom: 0; }
</style>
</head>
<body>
<div class="canvas">
  <section class="card">
    <div class="brand">
      <span class="brand-mark"></span>
      <span class="brand-name">Calvorn</span>
    </div>
    <div class="brand-sub">Construction, Inc</div>

    <div class="contact">
      <p class="address">2170 Ridgeline Road<br>Calder Valley AB 2170</p>
      <p class="contact-line">
        <svg viewBox="0 0 20 20" aria-hidden="true"><path fill="#f07a2e" d="M4 2l4 1 1 4-2 1.5a11 11 0 005 5L13.5 11l4 1 1 4-2 2C9 18 2 11 2 4z"/></svg>
        555.210.4471
      </p>
      <p class="contact-line">
        <svg viewBox="0 0 20 20" aria-hidden="true"><rect x="1" y="4" width="18" height="12" fill="#f07a2e"/><path d="M1 4l9 7 9-7" fill="none" stroke="#262626" stroke-width="1.6"/></svg>
        info@calvornconstruction.com
      </p>
      <p class="contact-line">
        <svg viewBox="0 0 20 20" aria-hidden="true"><circle cx="10" cy="10" r="8" fill="#f07a2e"/><path d="M2 10h16M10 2c-4 4-4 12 0 16M10 2c4 4 4 12 0 16" fill="none" stroke="#262626" stroke-width="1.3"/></svg>
        www.calvornconstruction.com
      </p>
    </div>

    <div class="person">
      <p class="person-name">Dane Morrow</p>
      <p class="person-title">CEO/Founder</p>
    </div>
    <span class="person-bar"></span>

    <svg class="hazard-strip" width="640" height="24" viewBox="0 0 640 24" aria-hidden="true">
      <g fill="#f07a2e">
        <polygon points="0,0 16,0 25,24 9,24"/>
        <polygon points="30,0 46,0 55,24 39,24"/>
        <polygon points="60,0 76,0 85,24 69,24"/>
        <polygon points="90,0 106,0 115,24 99,24"/>
        <polygon points="120,0 136,0 145,24 129,24"/>
        <polygon points="150,0 166,0 175,24 159,24"/>
        <polygon points="180,0 196,0 205,24 189,24"/>
        <polygon points="210,0 226,0 235,24 219,24"/>
        <polygon points="240,0 256,0 265,24 249,24"/>
        <polygon points="270,0 286,0 295,24 279,24"/>
        <polygon points="300,0 316,0 325,24 309,24"/>
        <polygon points="330,0 346,0 355,24 339,24"/>
        <polygon points="360,0 376,0 385,24 369,24"/>
        <polygon points="390,0 406,0 415,24 399,24"/>
        <polygon points="420,0 436,0 445,24 429,24"/>
        <polygon points="450,0 466,0 475,24 459,24"/>
        <polygon points="480,0 496,0 505,24 489,24"/>
        <polygon points="510,0 526,0 535,24 519,24"/>
        <polygon points="540,0 556,0 565,24 549,24"/>
        <polygon points="570,0 586,0 595,24 579,24"/>
        <polygon points="600,0 616,0 625,24 609,24"/>
      </g>
    </svg>
  </section>
</div>
</body>
</html>
```